Builder of high-end, expensive tables and other furniture

Build a website that represents what we do. I want a luxury feel that appeals to those who can afford our products. We build very high end tables and other furniture using trees that have fallen or are standing dead. We never cut living trees. Trees are harvested, milled, and kiln dried. Then that lumber is meticulously turned into fine furniture using the best equipment. Our furniture prices range from $1,000-$20,000.

Trying to figure out how to raise my spend.

```html
<!DOCTYPE html>
<html lang="en">
<head>
<meta charset="utf-8">
<title>Hearthwood Tables — Crafting Extraordinary Furniture</title>
<link rel="stylesheet" href="https://fonts.googleapis.com/css2?family=Cinzel:wght@400;500&family=Montserrat:wght@400;500;600&display=swap">
<style>
:root{
  --peach:#fde8dc;
  --orange:#f07022;
  --blue:#0a52ad;
  --sky:#c9d9ec;
  --ink:#1e1e1e;
  --muted:#555;
  --dark:#2a2a2a;
  --darker:#1d1d1d;
  --white:#ffffff;
}
*{margin:0;padding:0;box-sizing:border-box}
html,body{width:1200px;height:4691px;overflow:hidden;background:var(--white)}
body{position:relative;font-family:'Montserrat',sans-serif;color:var(--ink)}
.abs{position:absolute}
.photo{position:absolute}
.display{font-family:'Cinzel',serif;font-weight:400;color:var(--ink);line-height:1.05;white-space:nowrap;z-index:3}

/* header */
.brand{position:absolute;display:flex;align-items:center;gap:9px;font-family:'Montserrat',sans-serif;font-weight:600;font-size:23px;color:var(--orange);letter-spacing:-.3px}
.brand-dot{width:18px;height:18px;border-radius:50%;background:var(--orange)}
.nav{position:absolute;left:527px;top:48px;display:flex;align-items:center;gap:40px;font-size:11px;letter-spacing:2px;color:var(--ink)}
.nav a{color:inherit;text-decoration:none}
.nav .active{border-bottom:1px solid var(--orange);padding-bottom:6px}
.nav .sep{width:5px;height:5px;border-radius:50%;background:var(--orange)}

.hero-bg{left:0;top:0;width:1200px;height:736px;background:var(--peach)}
.hero-title{font-size:58px}
.badge{position:absolute;width:100px;height:100px}

.vline{position:absolute;width:1px;background:#777}

/* intro */
.intro-title{left:197px;top:970px;font-size:38px;line-height:1.2}
.intro-copy{left:197px;top:1092px;width:285px;font-size:10.5px;line-height:21px;color:var(--muted)}
.intro-copy p+p{margin-top:20px}
.btn{position:absolute;display:flex;align-items:center;justify-content:center;gap:18px;color:var(--white);font-size:9px;font-weight:600;letter-spacing:5px}
.btn-orange{background:var(--orange)}
.btn-blue{background:var(--blue)}

/* values */
.values-band{left:0;top:1524px;width:1200px;height:457px;background:var(--sky)}
.values-title{left:0;top:1612px;width:1200px;text-align:center;font-size:52px;line-height:1.2}
.value-card{left:91px;top:1655px;width:324px;height:424px;background:var(--blue);color:var(--white);text-align:center;padding:60px 34px 0}
.value-card h3{font-weight:500;font-size:27px;line-height:1.25}
.value-card p{margin-top:22px;font-size:10px;line-height:21px;font-weight:500}
.icon-ring{position:absolute;width:68px;height:68px;border-radius:50%;background:var(--white);border:1px dashed var(--blue)}

/* featured */
.featured-title{right:198px;top:2370px;text-align:right;font-size:42px;line-height:1.2}
.circle-btn{position:absolute;width:40px;height:40px;border-radius:50%;display:flex;align-items:center;justify-content:center}
.card-label{position:absolute;left:30px;bottom:30px;color:var(--white)}
.card-label h4{font-size:14px;font-weight:600}
.card-label p{margin-top:16px;font-size:9.5px;line-height:19px;width:200px}

/* quote */
.quote-band{left:0;top:2895px;width:384px;height:640px;background:var(--peach)}
.quote-text{left:710px;top:3095px;font-size:29px;line-height:45px}

/* collection */
.collection-title{left:0;top:3620px;width:1200px;text-align:center;font-size:54px;line-height:1.2}
.footer-bg{left:0;top:3900px;width:1200px;height:791px}
.strip{position:absolute;left:-40px;top:3880px;width:1300px;transform:rotate(-6deg);transform-origin:left top;display:grid;grid-template-columns:repeat(5,250px);gap:16px 14px;z-index:1}
.tile{height:190px}

/* footer */
.footer-h{position:absolute;font-size:13px;color:var(--white);letter-spacing:.5px}
.footer-links{position:absolute;left:570px;top:4372px;list-style:none;font-size:11px;color:#ddd}
.footer-links li{height:49px}
.input{position:absolute;left:197px;top:4454px;width:255px;height:32px;background:var(--white);font-size:7px;color:#777;padding:11px 12px}
.contact{left:757px;top:4298px;width:246px;height:257px;background:var(--darker)}
.contact-item{position:absolute;left:35px;display:flex;gap:16px;align-items:center;color:#ddd}
.contact-item small{display:block;font-size:6px;font-weight:600;letter-spacing:1px;margin-bottom:3px}
.contact-item span{font-size:8px}
.copy{position:absolute;left:197px;top:4660px;font-size:9px;color:#ccc}
.social{position:absolute;top:4656px;width:18px;height:18px;border-radius:50%;background:var(--white)}
</style>
</head>
<body>

<!-- HERO -->
<div class="abs hero-bg"></div>
<div class="brand" style="left:197px;top:38px"><span class="brand-dot"></span>Hearthwood Tables</div>
<nav class="nav">
  <a class="active">HOME</a><span class="sep"></span>
  <a>SERVICES</a><span class="sep"></span>
  <a>ABOUT</a><span class="sep"></span>
  <a>OUR PRODUCTS</a>
</nav>

<h1>
  <span class="abs display hero-title" style="left:197px;top:148px">Crafting</span>
  <span class="abs display hero-title" style="left:330px;top:224px">Extraordinary</span>
  <span class="abs display hero-title" style="right:197px;top:300px">Furniture</span>
</h1>

<svg class="badge" style="left:910px;top:130px" viewBox="0 0 100 100" aria-label="Scroll down">
  <defs><path id="ring1" d="M50,50 m-38,0 a38,38 0 1,1 76,0 a38,38 0 1,1 -76,0"/></defs>
  <text font-family="Montserrat,sans-serif" font-size="7.5" letter-spacing="3" fill="#222"><textPath href="#ring1">SCROLL DOWN • SCROLL DOWN •</textPath></text>
  <circle cx="50" cy="50" r="17" fill="#0a52ad"/>
  <text x="50" y="54" text-anchor="middle" font-family="Montserrat,sans-serif" font-size="11" fill="#fff">0</text>
</svg>

<div class="photo" role="img" aria-label="Wooden console table with lamp and plant against a pale wall" style="left:0;top:515px;width:222px;height:361px;background:linear-gradient(180deg,#ecebe7 0%,#e3ddd3 55%,#a4774b 70%,#ddd3c4 100%)"></div>
<div class="photo" role="img" aria-label="Slatted oak sideboard beside a potted palm in a bright room" style="left:335px;top:342px;width:530px;height:446px;background:linear-gradient(180deg,#ebebea 0%,#e5e3df 55%,#c99a62 62%,#d3ad7e 78%,#c9a88a 100%)"></div>
<div class="photo" role="img" aria-label="Dining table by sheer curtains" style="left:1038px;top:401px;width:162px;height:291px;background:linear-gradient(180deg,#f2efe9 0%,#e9e2d5 60%,#9a7556 100%)"></div>
<div class="photo" role="img" aria-label="Wooden chair with woven seat" style="left:787px;top:708px;width:122px;height:140px;background:linear-gradient(180deg,#f0ece6 0%,#d8b486 60%,#c19566 100%)"></div>
<div class="vline" style="left:601px;top:789px;height:50px"></div>

<!-- INTRO -->
<div class="photo" role="img" aria-label="Bentwood chair with woven seat holding books and a green leaf" style="left:532px;top:1021px;width:471px;height:392px;background:linear-gradient(160deg,#e4e2df 0%,#dcd7cf 45%,#c99e6b 70%,#a8794c 100%)"></div>
<h2 class="abs display intro-title">Unleashing The Art<br>Of Fine Furniture</h2>
<div class="abs intro-copy">
  <p>Lorem Ipsum is simply dummy text of the printing and typesetting industry. Lorem Ipsum has been the industry's standard dummy text ever since the 1500s, when an unknown printer took a galley of type and scrambled it to make a type specimen book. It has survived not only five centuries, but also the leap into electronic typesetting, remaining essentially unchanged. It was popularised in the 1960s with the release of Letraset sheets containing.</p>
  <p>Lorem Ipsum passages, and more recently with desktop publishing software like Aldus PageMaker including versions of Lorem Ipsum.</p>
</div>
<div class="btn btn-orange" style="left:803px;top:1377px;width:200px;height:36px">LEARN MORE
  <svg width="22" height="8" viewBox="0 0 22 8"><path d="M0 4H20M16 1l4 3-4 3" stroke="#fff" fill="none"/></svg></div>
<div class="vline" style="left:608px;top:1365px;height:97px"></div>

<!-- CORE VALUES -->
<div class="abs values-band"></div>
<h2 class="abs display values-title">Our Core<br>Values</h2>
<div class="abs value-card">
  <h3>Product Durability<br>And Reliability</h3>
  <p>Lorem Ipsum is simply dummy text of the printing and typesetting industry. Lorem Ipsum has been the industry's standard dummy text ever since the 1500s, when an unknown printer took a galley of type and scrambled it to make a type specimen book. It has survived not only five centuries, but also the leap into electronic typesetting.</p>
</div>
<div class="icon-ring" style="left:219px;top:2044px"><svg width="66" height="66" viewBox="0 0 66 66"><path d="M24 42L42 24M32 24h10v10" stroke="#333" fill="none"/></svg></div>
<div class="photo" role="img" aria-label="Wooden side table with ceramic lamp and books on a woven rug" style="left:437px;top:1792px;width:324px;height:424px;background:linear-gradient(180deg,#f1eeea 0%,#e7e2da 35%,#b88656 50%,#a56e40 65%,#c69a78 100%)"></div>
<div class="photo" role="img" aria-label="Round oak table with grey chair and potted plant" style="left:785px;top:1655px;width:324px;height:424px;background:linear-gradient(180deg,#e9e6dc 0%,#e2dfd6 40%,#b8955d 52%,#cfb58c 75%,#b89a7a 100%)"></div>

<!-- FEATURED PRODUCTS -->
<div class="circle-btn" style="left:124px;top:2362px;background:var(--orange)"><svg width="20" height="8" viewBox="0 0 20 8"><path d="M0 4H18M14 1l4 3-4 3" stroke="#fff" fill="none"/></svg></div>
<div class="circle-btn" style="left:124px;top:2413px;border:1px solid var(--orange)"><svg width="20" height="8" viewBox="0 0 20 8"><path d="M20 4H2M6 1L2 4l4 3" stroke="#222" fill="none"/></svg></div>
<div class="photo" role="img" aria-label="Pine cabinet with framed prints and dried grasses in a vase" style="left:197px;top:2364px;width:344px;height:397px;background:linear-gradient(180deg,#dcdbd9 0%,#cfcdca 35%,#b57a47 52%,#8e5a30 100%)">
  <div class="card-label"><h4>Lorem Ipsum</h4><p>Lorem Ipsum is simply dummy text of the printing and typesetting industry.</p></div>
  <div class="circle-btn" style="left:270px;top:332px;background:#fff"><svg width="18" height="8" viewBox="0 0 18 8"><path d="M0 4H16M12 1l4 3-4 3" stroke="#222" fill="none"/></svg></div>
</div>
<h2 class="abs display featured-title">Our Featured<br>Products</h2>
<div class="photo" role="img" aria-label="Carved wooden bowl chair by a window" style="left:559px;top:2495px;width:231px;height:266px;background:linear-gradient(180deg,#efebe4 0%,#e6dfd4 45%,#b98552 70%,#ddd3c7 100%)"></div>
<div class="photo" role="img" aria-label="Mid-century wooden sideboard with vases" style="left:809px;top:2495px;width:231px;height:266px;background:linear-gradient(180deg,#f1f0ed 0%,#ebe9e5 50%,#b77a45 68%,#cdb9a3 100%)"></div>
<div class="photo" role="img" aria-label="Oak drawer unit with black frame" style="left:1060px;top:2495px;width:140px;height:266px;background:linear-gradient(180deg,#c69361 0%,#a8723e 45%,#2b2521 60%,#b17c49 100%)"></div>

<!-- QUOTE -->
<div class="abs quote-band"></div>
<div class="photo" role="img" aria-label="Craftsman cutting a fallen log with a chainsaw" style="left:197px;top:2950px;width:462px;height:532px;background:linear-gradient(160deg,#4e4a35 0%,#6b5c3c 40%,#b57c4a 65%,#c8a57a 85%,#8a7a5a 100%)"></div>
<div class="btn btn-blue" style="left:461px;top:3445px;width:198px;height:37px">GET STARTED
  <svg width="22" height="8" viewBox="0 0 22 8"><path d="M0 4H20M16 1l4 3-4 3" stroke="#fff" fill="none"/></svg></div>
<svg class="abs" style="left:889px;top:2968px" width="114" height="80" viewBox="0 0 114 80">
  <path d="M2 78V30L22 2h16L24 30h24v48Z M64 78V30L84 2h16L86 30h26v48Z" fill="none" stroke="#f07022" stroke-width="4" stroke-linejoin="round"/>
</svg>
<p class="abs display quote-text">Lumber Is<br>Meticulously<br>Turned Into Fine<br>Furniture Using<br>The Best<br>Equipment</p>

<!-- COLLECTION -->
<svg class="badge" style="left:196px;top:3628px" viewBox="0 0 100 100" aria-label="Scroll to view more">
  <defs><path id="ring2" d="M50,50 m-38,0 a38,38 0 1,1 76,0 a38,38 0 1,1 -76,0"/></defs>
  <text font-family="Montserrat,sans-serif" font-size="7.5" letter-spacing="3" fill="#222"><textPath href="#ring2">SCROLL TO VIEW • MORE ITEMS •</textPath></text>
  <circle cx="50" cy="50" r="17" fill="#0a52ad"/>
  <text x="50" y="54" text-anchor="middle" font-family="Montserrat,sans-serif" font-size="11" fill="#fff">0</text>
</svg>
<h2 class="abs display collection-title">Our<br>Collection</h2>

<svg class="abs footer-bg" viewBox="0 0 1200 791" preserveAspectRatio="none"><polygon points="0,343 1200,200 1200,791 0,791" fill="#2a2a2a"/></svg>

<div class="strip">
  <div class="tile" role="img" aria-label="Stacked firewood with black chair" style="background:linear-gradient(135deg,#8a5a35,#c48a55 50%,#2a2a2a)"></div>
  <div class="tile" role="img" aria-label="Wooden spindle chair" style="background:linear-gradient(180deg,#f1ece4,#d19b5a 60%,#e6d7c4)"></div>
  <div class="tile" role="img" aria-label="Small wooden chest of drawers" style="background:linear-gradient(180deg,#f4f1ec,#eee8df 50%,#c58a55 75%,#eadfd2)"></div>
  <div class="tile" role="img" aria-label="White pedestal table with wooden chair" style="background:linear-gradient(180deg,#f3ece2,#e2cdb0 60%,#c49a6a)"></div>
  <div class="tile" role="img" aria-label="Low wooden dresser in a bright room" style="background:linear-gradient(180deg,#f6f4f1,#e9e3db 60%,#b98453)"></div>
  <div class="tile" role="img" aria-label="Close view of joined oak boards" style="background:linear-gradient(135deg,#a8693a,#d39a62 50%,#7f4c28)"></div>
  <div class="tile" role="img" aria-label="Carved bowl chair by curtains" style="background:linear-gradient(180deg,#efe9e0,#c08b58 60%,#e0d5c8)"></div>
  <div class="tile" role="img" aria-label="Dining set with wooden chairs" style="background:linear-gradient(180deg,#f2efea,#e5ddd2 40%,#6a4a30 75%,#d8cbbb)"></div>
  <div class="tile" role="img" aria-label="Table with orange chairs and plants" style="background:linear-gradient(180deg,#f4f2ee,#e8e2d8 50%,#c6703a 70%,#ebe5dc)"></div>
  <div class="tile" role="img" aria-label="Bentwood chair detail" style="background:linear-gradient(180deg,#eee9e2,#c48c52 55%,#d8c6ae)"></div>
</div>

<!-- FOOTER -->
<div class="brand" style="left:197px;top:4322px"><span class="brand-dot"></span>Hearthwood Tables</div>
<div class="footer-h" style="left:197px;top:4410px">NEWSLETTER</div>
<div class="abs" style="left:197px;top:4430px;width:60px;height:1px;background:#fff"></div>
<div class="input">YOUR EMAIL</div>
<div class="btn btn-blue" style="left:197px;top:4494px;width:157px;height:37px;background:linear-gradient(90deg,#0a52ad,#3f86d6)">SIGN UP
  <svg width="22" height="8" viewBox="0 0 22 8"><path d="M0 4H20M16 1l4 3-4 3" stroke="#fff" fill="none"/></svg></div>

<div class="footer-h" style="left:570px;top:4320px">QUICK LINKS</div>
<div class="abs" style="left:570px;top:4340px;width:40px;height:1px;background:#fff"></div>
<ul class="footer-links">
  <li>HOME</li><li>SERVICES</li><li>ABOUT</li><li>OUR PRODUCTS</li>
</ul>

<div class="abs contact">
  <div class="footer-h" style="left:35px;top:36px">CONTACT</div>
  <div class="abs" style="left:35px;top:56px;width:40px;height:1px;background:#fff"></div>
  <div class="contact-item" style="top:86px">
    <svg width="14" height="10" viewBox="0 0 14 10"><rect width="14" height="10" fill="#fff"/><path d="M0 0l7 5 7-5" stroke="#1d1d1d" fill="none"/></svg>
    <div><small>MAIL</small><span>hello@hearthwood.example</span></div>
  </div>
  <div class="contact-item" style="top:143px">
    <svg width="14" height="14" viewBox="0 0 14 14"><path d="M1 6L13 1 8 13 6.5 7.5Z" fill="#fff"/></svg>
    <div><small>ADDRESS</small><span>Lorem Ipsum is simply dummy</span></div>
  </div>
  <div class="contact-item" style="top:200px">
    <svg width="14" height="14" viewBox="0 0 24 24"><path d="M6.6 10.8a15 15 0 006.6 6.6l2.2-2.2a1 1 0 011-.25 11.4 11.4 0 003.6.6 1 1 0 011 1V20a1 1 0 01-1 1A17 17 0 013 4a1 1 0 011-1h3.5a1 1 0 011 1c0 1.25.2 2.45.6 3.6a1 1 0 01-.25 1Z" fill="#fff"/></svg>
    <div><small>PHONE</small><span style="font-size:11px">555-014-2290</span></div>
  </div>
</div>

<div class="copy">© Hearthwood Tables 2023. All Rights Reserved.</div>
<div class="social" style="left:950px"></div>
<div class="social" style="left:983px"></div>

</body>
</html>
```